Brindle Barks Chews Pouch Design

I want a pouch design for my yak cheese dog chews. My competitor is golden tail, see attached. I want something minimalist like that where you see that there is only 3 ingredients, Yak milk, lime juice, Himalayan salt. I want it to say 100% natural 100% organic on it. Also odor free. There has to be a big see through window on it so you can see the products inside. Here is my logo and my competitor package. The package is 13cm x 17cm x 5cm. I have 5 sizes of bags to create but same image design

Target Market(s)

Pet owners

Industry/Entity Type

Dog products

Requirements
Must have
• « SMALL » « MIN NET WT 200 g / 5 PCS » and its important the 3 ingredients mentioned and 100% natural and organic must be very visible however the window must be big
Should not have
• The ingredients in the back

```html
<!DOCTYPE html>
<html lang="en">
<head>
<meta charset="utf-8">
<title>Brindle Barks Chews – Yak Cheese Dog Chews Pouch</title>
<link rel="stylesheet" href="https://fonts.googleapis.com/css2?family=Chewy&family=Nunito:wght@900&display=swap">
<style>
  :root {
    --pouch-orange: #f8a12e;
    --cream: #fdf8dc;
    --maroon: #6a2029;
    --window-amber: #e08a2a;
    --window-deep: #a4471c;
    --window-gold: #f2a545;
    --page: #ffffff;
  }
  * { margin: 0; padding: 0; box-sizing: border-box; }
  html, body {
    width: 939px;
    height: 1200px;
    overflow: hidden;
    background: var(--page);
  }
  .pouch { display: block; width: 939px; height: 1200px; }
  .display-type { font-family: "Chewy", cursive; }
  .label-type { font-family: "Nunito", sans-serif; font-weight: 900; }
  .outlined {
    paint-order: stroke fill;
    stroke-linejoin: round;
  }
</style>
</head>
<body>
<svg class="pouch" viewBox="0 0 939 1200" xmlns="http://www.w3.org/2000/svg">
  <defs>
    <linearGradient id="window-fill" x1="0" y1="0" x2="1" y2="0">
      <stop offset="0" stop-color="var(--window-deep)"/>
      <stop offset="0.25" stop-color="var(--window-amber)"/>
      <stop offset="0.55" stop-color="var(--window-gold)"/>
      <stop offset="0.8" stop-color="var(--window-amber)"/>
      <stop offset="1" stop-color="var(--window-deep)"/>
    </linearGradient>
    <path id="ingredient-curve" d="M 70 975 C 300 1030, 560 900, 880 870"/>
  </defs>

  <!-- pouch body -->
  <rect class="pouch-body" width="939" height="1200" fill="var(--pouch-orange)"/>

  <!-- hang hole -->
  <rect class="hang-hole" x="418" y="34" width="115" height="36" rx="18" fill="var(--page)"/>
  <rect class="hang-hole-stem" x="466" y="22" width="18" height="20" rx="9" fill="var(--page)"/>

  <!-- cream band framing the window -->
  <path class="cream-band" fill="var(--cream)"
        d="M 0 290 C 250 230, 520 360, 939 150 L 939 1000 C 620 1020, 320 1120, 0 1090 Z"/>

  <!-- product window -->
  <path class="product-window" role="img" aria-label="See-through window showing the yak cheese chews inside"
        fill="url(#window-fill)"
        d="M 53 360 L 890 360 L 890 820 C 620 850, 330 930, 53 925 Z"/>

  <!-- lower orange base -->
  <path class="pouch-base" fill="var(--pouch-orange)"
        d="M 0 1085 C 320 1110, 620 985, 939 965 L 939 1200 L 0 1200 Z"/>

  <!-- odor free ribbon -->
  <g class="odor-free-ribbon">
    <rect x="771" y="0" width="94" height="180" fill="var(--maroon)"/>
    <circle cx="818" cy="138" r="42" fill="var(--maroon)"/>
    <circle cx="818" cy="138" r="34" fill="none" stroke="var(--cream)" stroke-width="2"/>
    <path d="M 800 120 L 836 156" stroke="var(--cream)" stroke-width="3" stroke-linecap="round"/>
    <path d="M 812 124 C 804 132, 826 138, 816 148 C 812 152, 818 156, 820 158" fill="none" stroke="var(--cream)" stroke-width="3" stroke-linecap="round"/>
    <text class="label-type" x="818" y="117" font-size="7" fill="var(--cream)" text-anchor="middle">ODOR FREE</text>
    <text class="label-type" x="818" y="165" font-size="7" fill="var(--cream)" text-anchor="middle">ODOR FREE</text>
  </g>

  <!-- brand mark -->
  <g class="brand">
    <circle cx="230" cy="250" r="118" fill="var(--cream)"/>
    <text class="display-type" x="135" y="240" font-size="40" textLength="190" lengthAdjust="spacingAndGlyphs" fill="var(--maroon)">Brindle Barks</text>
    <text class="display-type" x="180" y="288" font-size="40" textLength="100" lengthAdjust="spacingAndGlyphs" fill="var(--maroon)">Chews</text>
  </g>

  <!-- product title -->
  <g class="product-title display-type" fill="var(--maroon)">
    <text class="outlined" x="425" y="320" font-size="96" textLength="450" lengthAdjust="spacingAndGlyphs" stroke="var(--cream)" stroke-width="10" transform="rotate(-7 650 290)">YAK CHEESE</text>
    <text class="outlined" x="425" y="435" font-size="96" textLength="450" lengthAdjust="spacingAndGlyphs" stroke="var(--cream)" stroke-width="10" transform="rotate(-7 650 405)">DOG CHEWS</text>
  </g>

  <!-- natural & organic claim -->
  <g class="claim display-type" fill="var(--cream)" stroke="var(--maroon)">
    <text class="outlined" x="95" y="625" font-size="160" textLength="320" lengthAdjust="spacingAndGlyphs" stroke-width="12">100%</text>
    <text class="outlined" x="95" y="740" font-size="104" textLength="320" lengthAdjust="spacingAndGlyphs" stroke-width="10">NATURAL</text>
    <text class="outlined" x="95" y="855" font-size="104" textLength="320" lengthAdjust="spacingAndGlyphs" stroke-width="10">ORGANIC</text>
    <text class="outlined" x="438" y="760" font-size="60" fill="var(--maroon)" stroke="var(--cream)" stroke-width="6">&amp;</text>
  </g>

  <!-- ingredients -->
  <text class="ingredients display-type" font-size="46" fill="var(--maroon)">
    <textPath href="#ingredient-curve" startOffset="20" textLength="790" lengthAdjust="spacingAndGlyphs">YAK MILK • LIME JUICE • HIMALAYAN SALT</textPath>
  </text>

  <!-- size & weight -->
  <g class="size-info label-type">
    <path class="net-weight-tag" d="M 442 1072 L 660 1060 L 660 1104 L 430 1114 Z" fill="var(--maroon)"/>
    <text x="450" y="1097" font-size="18" textLength="175" lengthAdjust="spacingAndGlyphs" fill="var(--cream)">MIN NET WT 200g</text>
    <path class="size-tag" d="M 760 1026 L 838 1016 L 842 1058 L 764 1066 Z" fill="var(--cream)"/>
    <text x="770" y="1052" font-size="17" textLength="62" lengthAdjust="spacingAndGlyphs" fill="var(--maroon)">SMALL</text>
    <circle class="piece-count" cx="702" cy="1057" r="58" fill="var(--maroon)" stroke="var(--cream)" stroke-width="5"/>
    <text x="702" y="1066" font-size="58" fill="var(--cream)" text-anchor="middle">5</text>
    <text x="702" y="1097" font-size="20" fill="var(--cream)" text-anchor="middle">PCS</text>
  </g>
</svg>
</body>
</html>
```